Forensic investigators looking for updated powerpoint design

Louisiana company called Harlow Vantage has an important upcoming meeting and needs a redesigned slideshow template. They are an engineering firm providing evaluation, reporting, and expert witness testimony on a variety of topics to support the litigation and insurance industries. The meeting in question will be held at a conference catering to insurance underwriters.

Target Market(s)

Upcoming tradeshow presentation

Industry/Entity Type

Insurance; TIC (Testing, Inspection, Certification)

Font styles to use
Sans Serif

Colors
0054AA
0677BA
7BADD7
CADEEF
E8F1F8
FFC000
F8CF3A
FAE287
FDF2CF
FEFAEE

Requirements
Must have
• Updated background template with examples of different layouts (bullet list w/ graphic, bullet list without, quote, large central photo, etc.), implementing company logo
Nice to have
• Visual motif that carries through powerpoint designs
Should not have
• No hexagons (old motif of parent company that we're moving away from)

```html
<!DOCTYPE html>
<html lang="en">
<head>
<meta charset="utf-8">
<title>Harlow Vantage – Slide Template</title>
<link href="https://fonts.googleapis.com/css2?family=Poppins:wght@400;500;600;800&display=swap" rel="stylesheet">
<style>
:root{
  --page:#9c9c9c;
  --slide:#f4f5f8;
  --blue:#0054aa;
  --blue-mid:#0677ba;
  --blue-light:#7badd7;
  --yellow:#ffc000;
  --ink:#111111;
  --muted:#8a8f98;
  --white:#ffffff;
}
*{margin:0;padding:0;box-sizing:border-box}
html,body{width:1200px;height:1090px;overflow:hidden}
body{background:var(--page);font-family:'Poppins',sans-serif;position:relative;color:var(--ink)}
.slide{position:absolute;width:482px;height:272px;background:var(--slide);overflow:hidden}
.col-left{left:99px}.col-right{left:618px}
.row-1{top:98px}.row-2{top:410px}.row-3{top:720px}
.photo{position:absolute;border-radius:50%;z-index:0}
.photo-cover{left:238px;top:-130px;width:520px;height:520px}
.photo-round{left:243px;top:-118px;width:356px;height:356px}
.title{position:absolute;left:26px;top:20px;font-weight:800;font-size:24px;line-height:23px;text-transform:uppercase;z-index:1}
.title .y{color:var(--yellow);display:block}
.title .b{color:var(--blue);display:block}
.title .l{color:var(--blue-light);display:block}
.cover-title{left:21px;top:24px;font-size:25.5px;line-height:25px}
.band{position:absolute;left:0;background:var(--yellow);color:var(--white);font-weight:500;z-index:2}
.cover-band{top:155px;height:28px;width:245px;clip-path:polygon(0 0,236px 0,245px 100%,0 100%);font-size:7.2px;line-height:9px;padding:5px 0 0 20px}
.brand{position:absolute;color:var(--blue);font-weight:600;display:flex;align-items:center;gap:3px;line-height:1;white-space:nowrap;z-index:1}
.brand .mark{background:var(--blue);border-radius:50%}
.cover-brand{left:20px;top:220px;font-size:17px}
.cover-brand .mark{width:12px;height:12px}
.cover-tag{position:absolute;left:36px;top:239px;font-size:5.2px;font-weight:600;color:var(--ink);letter-spacing:.2px}
.cover-url{position:absolute;left:20px;top:251px;font-size:6.2px;font-weight:500}
.footer .brand{left:26px;top:251px;font-size:7px}
.footer .brand .mark{width:5px;height:5px}
.footer .bar{position:absolute;left:102px;right:0;top:252px;height:7px;background:var(--blue);border-radius:4px 0 0 4px;z-index:1}
.outline{position:absolute;left:25px;top:78px;list-style:none;font-size:8px;font-weight:500;line-height:15px;z-index:1}
.outline li{display:flex;align-items:center;gap:4px}
.outline svg{width:6px;height:6px;flex:none}
.body{position:absolute;left:26px;font-size:8.2px;line-height:11px;font-weight:500;text-align:justify;letter-spacing:-.1px;z-index:1}
.stat{top:72px;width:184px}
.source{position:absolute;left:26px;top:123px;font-size:7px;color:var(--muted)}
.sub{position:absolute;left:25px;top:83px;color:var(--yellow);font-size:11px;line-height:11px;font-weight:500;z-index:1}
.quote{left:25px;top:117px;width:215px;font-size:8px;line-height:9.8px}
.quote-band{top:185px;height:46px;width:352px;clip-path:polygon(0 0,290px 0,352px 100%,0 100%);font-size:6.4px;line-height:9.6px;padding:8px 92px 0 25px}
.decay{top:51px;width:173px}
.decay p+p{margin-top:11px}
.lorem{left:25px;top:84px;width:213px}
</style>
</head>
<body>

<section class="slide col-left row-1">
  <div class="photo photo-cover" role="img" aria-label="Photo of steel gears resting on engineering blueprints" style="background:linear-gradient(135deg,#c9d0da,#eef1f5 45%,#9aa4b0)"></div>
  <h1 class="title cover-title"><span class="y">Harlow</span><span class="y">Vantage</span><span class="l">A Consulting</span><span class="b">Engineering</span><span class="b">Firm.</span></h1>
  <div class="band cover-band">Joined The Harlow Vantage Team as the Client Services Manager for North Carolina, South Carolina, and Virginia.</div>
  <div class="brand cover-brand"><span class="mark"></span>Harlow Vantage</div>
  <div class="cover-tag">Engineering.Inspection.Failure Analysis</div>
  <div class="cover-url">⊕ www.harlowvantage.com</div>
</section>

<section class="slide col-right row-1">
  <div class="photo photo-round" role="img" aria-label="Photo of hard hat, level, tape measure and hand sketching a floor plan" style="background:linear-gradient(135deg,#f3d23a,#eceef0 50%,#d8dadd)"></div>
  <h2 class="title"><span class="y">Course</span><span class="b">Outline</span></h2>
  <ul class="outline">
    <li><svg viewBox="0 0 10 10"><circle cx="5" cy="5" r="4.2" fill="none" stroke="#ffc000" stroke-width="1.4"/><path d="M3 5.2l1.5 1.4L7 3.8" fill="none" stroke="#ffc000" stroke-width="1.4"/></svg>Purpose</li>
    <li><svg viewBox="0 0 10 10"><circle cx="5" cy="5" r="4.2" fill="none" stroke="#ffc000" stroke-width="1.4"/><path d="M3 5.2l1.5 1.4L7 3.8" fill="none" stroke="#ffc000" stroke-width="1.4"/></svg>Wood decay - "Biodeterioration"</li>
    <li><svg viewBox="0 0 10 10"><circle cx="5" cy="5" r="4.2" fill="none" stroke="#ffc000" stroke-width="1.4"/><path d="M3 5.2l1.5 1.4L7 3.8" fill="none" stroke="#ffc000" stroke-width="1.4"/></svg>How long does it take for a piece of wood to decay?</li>
    <li><svg viewBox="0 0 10 10"><circle cx="5" cy="5" r="4.2" fill="none" stroke="#ffc000" stroke-width="1.4"/><path d="M3 5.2l1.5 1.4L7 3.8" fill="none" stroke="#ffc000" stroke-width="1.4"/></svg>Mold, Decay and Fungus</li>
    <li><svg viewBox="0 0 10 10"><circle cx="5" cy="5" r="4.2" fill="none" stroke="#ffc000" stroke-width="1.4"/><path d="M3 5.2l1.5 1.4L7 3.8" fill="none" stroke="#ffc000" stroke-width="1.4"/></svg>Types of decay</li>
    <li><svg viewBox="0 0 10 10"><circle cx="5" cy="5" r="4.2" fill="none" stroke="#ffc000" stroke-width="1.4"/><path d="M3 5.2l1.5 1.4L7 3.8" fill="none" stroke="#ffc000" stroke-width="1.4"/></svg>Necessary Ingredients and Optimum Conditions</li>
    <li><svg viewBox="0 0 10 10"><circle cx="5" cy="5" r="4.2" fill="none" stroke="#ffc000" stroke-width="1.4"/><path d="M3 5.2l1.5 1.4L7 3.8" fill="none" stroke="#ffc000" stroke-width="1.4"/></svg>Sources of Moisture</li>
    <li><svg viewBox="0 0 10 10"><circle cx="5" cy="5" r="4.2" fill="none" stroke="#ffc000" stroke-width="1.4"/><path d="M3 5.2l1.5 1.4L7 3.8" fill="none" stroke="#ffc000" stroke-width="1.4"/></svg>Important Points</li>
    <li><svg viewBox="0 0 10 10"><circle cx="5" cy="5" r="4.2" fill="none" stroke="#ffc000" stroke-width="1.4"/><path d="M3 5.2l1.5 1.4L7 3.8" fill="none" stroke="#ffc000" stroke-width="1.4"/></svg>Results of Moisture Exposure Tests</li>
  </ul>
  <div class="footer"><div class="brand"><span class="mark"></span>Harlow Vantage</div><div class="bar"></div></div>
</section>

<section class="slide col-left row-2">
  <div class="photo photo-round" role="img" aria-label="Photo of stacked lumber inside a steel warehouse" style="background:linear-gradient(160deg,#5d7c8c,#6c5a4a 45%,#c9a27a)"></div>
  <h2 class="title"><span class="y">Interesting</span><span class="b">Statistic</span></h2>
  <p class="body stat">Current estimates show that replacement materials, needed to repair damage caused by rot alone, account for nearly 10 percent of U.S. annual wood production.</p>
  <p class="source">(Midland State University Extension)</p>
  <div class="footer"><div class="brand"><span class="mark"></span>Harlow Vantage</div><div class="bar"></div></div>
</section>

<section class="slide col-right row-2">
  <div class="photo photo-round" role="img" aria-label="Photo of hard hat, level, tape measure and hand sketching a floor plan" style="background:linear-gradient(135deg,#f3d23a,#eceef0 50%,#d8dadd)"></div>
  <h2 class="title"><span class="y">Wood</span><span class="b">Decay (Rot)</span></h2>
  <p class="sub">How long does it Take<br>for a Piece of Wood to Decay?</p>
  <p class="body quote">"There is no way even to crudely estimate the rate of wood decay or its age. Wood decay is a complex biological phenomenon subject to many physical and environmental factors, such as moisture level, temperature, wood species, fungus species, geographic locality, and climate"</p>
  <div class="band quote-band">Dana R. Whitfield, Biological Technician with the National Timber Research Laboratory Reference: Rot Never Sleeps All it takes is some wood and a little moisture - By Martin Kessel, July 12, 1999.</div>
  <div class="footer"><div class="brand"><span class="mark"></span>Harlow Vantage</div><div class="bar"></div></div>
</section>

<section class="slide col-left row-3">
  <div class="photo photo-round" role="img" aria-label="Close-up photo of rotting wood sill with fungal decay" style="background:linear-gradient(160deg,#8b8f8c,#b07a55 40%,#d9c7bb 70%,#9a5a3e)"></div>
  <h2 class="title"><span class="y">Decay</span></h2>
  <div class="body decay">
    <p>Decay fungus may appear as fan-shaped patches, strands, or root-like structures that are usually white or brown in color.</p>
    <p>Sometimes fruiting bodies are produced that take the form of mushrooms, brackets, or crusts. The fungus, in the form of microscopic, threadlike strands called hyphae, permeates the wood and uses parts of it as food.</p>
  </div>
  <div class="footer"><div class="brand"><span class="mark"></span>Harlow Vantage</div><div class="bar"></div></div>
</section>

<section class="slide col-right row-3">
  <div class="photo photo-round" role="img" aria-label="Photo of an unfinished concrete block house under a blue sky" style="background:linear-gradient(180deg,#3f74b8,#9fb8d0 45%,#b9b6ad 65%,#8a7a62)"></div>
  <h2 class="title"><span class="y">Heading</span><span class="b">Goes Here</span></h2>
  <p class="body lorem">Lorem ipsum dolor sit amet, consectetuer adipiscing elit, sed diam nonummy nibh euismod tincidunt ut laoreet dolore magna aliquam erat volutpat. Ut wisi enim ad minim veniam, quis nostrud exerci tation ullamcorper suscipit lobortis nisl ut aliquip ex ea commodo consequat. Duis autem vel eum iriure dolor in hendrerit in vulputate velit esse molestie consequat, vel illum dolore eu feugiat nulla facilisis at vero eros et accumsan et iusto odio dignissim qui blandit praesent luptatum zzril delenit augue duis dolore te feugait nulla facilisi.</p>
  <div class="footer"><div class="brand"><span class="mark"></span>Harlow Vantage</div><div class="bar"></div></div>
</section>

</body>
</html>
```